Gutschein für Onlineshop DIN A Lang
Zielgruppe
Wir betreiben unter www.feldkiste-online.example einen Onlineshop für Armee- und Outdoorbekleidung sowie Ausrüstung. Für eine Paketbeilage benötigen wir einen Gutschein
Aufgabenstellung
Erstellung eines Gutscheins im DIN A Lang Format (Kuvert) mit Vorder- und Rückseite im CI der Webseite. Logo kann gerne zur Verfügung gestellt werden.
Gutscheincode, Wert und Laufzeit wird noch mitgeteilt.

```html
<!DOCTYPE html>
<html lang="de">
<head>
<meta charset="utf-8">
<title>Gutschein Feldkiste – Vorder- und Rückseite</title>
<link rel="stylesheet" href="https://fonts.googleapis.com/css2?family=Stardos+Stencil:wght@700&family=Signika:wght@700&family=Arimo:wght@400;700&display=swap">
<style>
  :root {
    --olive-dark: #464830;
    --olive-light: #c2c898;
    --olive-mid: #8f9a63;
    --brown-ink: #4d4533;
    --text-dark: #3a3a2e;
    --bark-1: #4a3526;
    --bark-2: #6b4d37;
    --bark-3: #2e2219;
    --paper: #ffffff;
  }
  * { margin: 0; padding: 0; box-sizing: border-box; }
  html, body { width: 1190px; height: 1200px; overflow: hidden; background: var(--paper); }
  .canvas { position: relative; width: 1190px; height: 1200px; }

  .voucher { position: absolute; left: 0; width: 1190px; }
  .voucher--front { top: 0; height: 551px; }
  .voucher--back { top: 627px; height: 573px; }

  .photo {
    position: absolute;
    background:
      radial-gradient(ellipse at 35% 30%, var(--bark-2) 0%, transparent 55%),
      radial-gradient(ellipse at 75% 40%, #7a5a44 0%, transparent 50%),
      linear-gradient(160deg, var(--bark-1), var(--bark-3));
  }
  .voucher--front .photo { left: 0; top: 0; width: 942px; height: 551px; }
  .voucher--back .photo { left: 283px; top: 0; width: 907px; height: 573px; }

  .side-panel { position: absolute; background: var(--olive-light); }
  .voucher--front .side-panel { left: 942px; top: 0; width: 248px; height: 551px; }
  .voucher--back .side-panel { left: 0; top: 0; width: 283px; height: 573px; }

  .title-band {
    position: absolute; left: 0; top: 241px; width: 749px; height: 187px;
    background: var(--olive-dark);
    display: flex; align-items: center; justify-content: center;
  }
  .title-band h1 {
    font-family: "Stardos Stencil", "Allerta Stencil", sans-serif;
    font-weight: 700; font-size: 112px; letter-spacing: 6px;
    color: var(--olive-mid); line-height: 1;
  }
  .tagline {
    position: absolute; left: 0; top: 443px; width: 746px; height: 48px;
    background: var(--olive-light);
    font-family: "Arimo", Arial, sans-serif; font-size: 21px;
    color: var(--text-dark); line-height: 48px; padding-left: 15px;
  }

  .value {
    position: absolute; left: 1052px; top: 205px;
    transform: translate(-50%, -50%) rotate(-90deg);
    font-family: "Stardos Stencil", "Allerta Stencil", serif;
    font-weight: 700; font-size: 150px; line-height: 1;
    color: var(--brown-ink); white-space: nowrap;
  }

  .brand {
    position: absolute;
    font-family: "Stardos Stencil", "Allerta Stencil", sans-serif;
    font-weight: 700; color: var(--olive-dark);
    line-height: 1; white-space: nowrap;
  }
  .voucher--front .brand { left: 966px; top: 445px; font-size: 38px; }
  .voucher--back .brand { left: 48px; top: 765px; font-size: 38px; position: absolute; }

  .address {
    position: absolute; left: 12px; top: 366px;
    font-family: "Signika", "Trebuchet MS", sans-serif;
    font-weight: 700; font-size: 16px; line-height: 21.6px;
    color: var(--text-dark);
  }
  .address p + p { margin-top: 21.6px; }

  .about {
    position: absolute; left: 524px; top: 354px; width: 666px; height: 199px;
    background: var(--olive-light);
    padding: 9px 12px 0 10px;
    font-family: "Arimo", Arial, sans-serif; font-weight: 700;
    font-size: 14px; line-height: 19.3px; color: var(--text-dark);
  }
  .about h2 { font-size: 15.5px; line-height: 19px; font-weight: 700; }
  .about p { width: 560px; }
</style>
</head>
<body>
<div class="canvas">

  <section class="voucher voucher--front" aria-label="Vorderseite">
    <div class="photo" role="img" aria-label="Foto: abgetragene braune Lederstiefel auf Rindenmulch"></div>
    <div class="title-band"><h1>GUTSCHEIN</h1></div>
    <div class="tagline">www.feldkiste-online.example - Online Shop für Bundeswehrkleidung</div>
    <aside class="side-panel">
    </aside>
    <div class="value">25€</div>
    <div class="brand">FELDKISTE</div>
  </section>

  <section class="voucher voucher--back" aria-label="Rückseite">
    <aside class="side-panel">
      <div class="brand" style="top:138px;">FELDKISTE</div>
      <div class="address">
        <p>Nordlager GmbH<br>Division Feldkiste<br>Am Lindenhang 7<br>12345 Musterstadt<br>Germany</p>
        <p>Tel.: 01234/5678900<br>Fax: 01234/5678901<br>mail: info@nordlager.example</p>
      </div>
    </aside>
    <div class="photo" role="img" aria-label="Foto: abgetragene braune Lederstiefel auf Rindenmulch, Nahaufnahme"></div>
    <div class="about">
      <h2>www.feldkiste-online.example</h2>
      <p>Seit fast 10 Jahren sind wir mit unserem großen Bundeswehr-Shop nun im Internet tätig. Bei uns finden Sie eine der größen Auswahl an Bundeswehrbekleidung und Armeebekleidung sowie umfangreiche Ausrüstung für Arbeit, Hobby und Freizeit. Angler, Jäger und andere Freizeitaktivisten finden hier alles was Sie in der freien Natur benötigen. Bekleidung der Bundeswehr (ob Neu- oder Gebrauchtware) ist besonders robust und langlebig und deshalb auch für Beruf und Freizeit bestens geeignet. Wir freuen uns über Ihren Besuch auf www.feldkiste-online.example</p>
    </div>
  </section>

</div>
</body>
</html>
```